Lumacraftery 'Quiet Harbour' Book Cover Design project

I need to revise the book cover design I have for my coming book. The design I created through PixelGuild is great but the book has grown and changed so I'm looking for an alternative/option design. I can then choose later from the different options.

I need a book cover that represents the unique book I am creating.

Book Title:
The Open Meadow

Subtitle: Walking Forward Beyond Every Box

The book is targeting all readers with a special focus on same sex attracted readers. It should not have stereotypical images.

I am including a file of the book cover I have had designed. The back cover blurb, author info and author pic will remain the same. The colouring of the back cover and spine will, of course, change to match the colouring of the front cover.

The new title will be on the spine and the new title wording.

The front cover will be markedly different using the bold images and rainbow colours of the images found in the files I am uploading for you.

I am thinking of a large boldly coloured rainbow face with the title and subtitle ON the image. The image will be the whole cover. It will fill the cover as much as possible with the text added onto the pic.

The bold pictures I am including will give you the idea of what I'm looking for.

ANY of the images I've uploaded can be used as the actual front cover image OR the designer might have/find some suitable image to be used. The image is to be large and bold and fill the cover. Hopefully a positive energy.
It needs to be eye-catching and striking and bold and positive.

So...the book cover sample file I've provided can keep the back cover with completely new colouring. The front cover is completely new with new image, wording and energy.

It is to be a rainbow coloured face or figure for the cover image.

I hope that is clear enough for you. I'm very happy to discuss and clarify these ideas with the designer. Looking forward to another great PixelGuild experience.

Target Market(s)

Wide audience with special focus on Same Sex Attracted individuals

Font styles to use
Script
Other font styles liked:
• Some form of handwriting font to make the book title and text appear more personal....as if handwritten by me.

Requirements
Must have
• Boldness, Quirky, Rainbow Colour, Image to fill the cover, maybe dark cover contrasting background.
Nice to have
• A well balanced back cover especially in the area where the barcode will be placed.
Should not have
• No stereotypical images

```html
<!DOCTYPE html>
<html lang="en">
<head>
<meta charset="utf-8">
<title>The Open Meadow — Cover</title>
<link href="https://fonts.googleapis.com/css2?family=Bebas+Neue&family=Open+Sans:wght@400;600&display=swap" rel="stylesheet">
<style>
  :root {
    --backdrop: #efe3b0;
    --paint-orange: #f06a23;
    --paint-red: #c9262a;
    --paint-blue: #2456b8;
    --paint-teal: #1e9a86;
    --paint-gold: #f4a623;
    --paint-navy: #1b2247;
    --paint-maroon: #7c1c2a;
    --band-white: #ffffff;
    --band-shade: #cdcdcd;
    --title-ink: #3b3b3b;
    --subtitle-ink: #7a7a7a;
    --author-ink: #ffffff;
  }
  * { margin: 0; padding: 0; box-sizing: border-box; }
  html, body {
    width: 1200px;
    height: 960px;
    overflow: hidden;
    background: var(--backdrop);
  }
  .stage {
    position: relative;
    width: 1200px;
    height: 960px;
  }
  .cover {
    position: absolute;
    left: 240px;
    top: 120px;
    width: 720px;
    height: 720px;
    overflow: hidden;
    box-shadow: 0 18px 40px rgba(120, 100, 40, 0.25);
  }
  .cover-art-upper {
    position: absolute;
    inset: 0 0 50% 0;
    background:
      radial-gradient(circle at 40% 45%, var(--paint-teal) 0, transparent 22%),
      radial-gradient(circle at 72% 60%, var(--paint-gold) 0, transparent 25%),
      radial-gradient(circle at 10% 70%, var(--paint-blue) 0, transparent 30%),
      linear-gradient(120deg, var(--paint-blue) 0%, var(--paint-red) 35%, var(--paint-orange) 60%, var(--paint-red) 100%);
  }
  .cover-art-lower {
    position: absolute;
    inset: 50% 0 0 0;
    background:
      radial-gradient(circle at 45% 40%, var(--paint-orange) 0, transparent 18%),
      radial-gradient(circle at 15% 30%, var(--paint-teal) 0, transparent 22%),
      linear-gradient(160deg, var(--paint-red) 0%, var(--paint-maroon) 45%, var(--paint-navy) 100%);
  }
  .title-band {
    position: absolute;
    left: 0;
    top: 340px;
    width: 720px;
    height: 170px;
  }
  .title-band svg {
    position: absolute;
    inset: 0;
    width: 100%;
    height: 100%;
  }
  .title-block {
    position: absolute;
    left: 240px;
    top: 50px;
  }
  .book-title {
    font-family: "Bebas Neue", sans-serif;
    font-size: 50px;
    letter-spacing: 3px;
    color: var(--title-ink);
    line-height: 1;
    text-transform: uppercase;
  }
  .book-subtitle {
    font-family: "Open Sans", sans-serif;
    font-size: 17px;
    color: var(--subtitle-ink);
    margin-top: 6px;
    letter-spacing: 0.2px;
  }
  .author-name {
    position: absolute;
    left: 90px;
    bottom: 52px;
    font-family: "Open Sans", sans-serif;
    font-weight: 600;
    font-size: 18px;
    color: var(--author-ink);
  }
</style>
</head>
<body>
<main class="stage">
  <section class="cover">
    <div class="cover-art-upper" role="img" aria-label="Palette-knife painting of a face in rainbow colours, upper part with the eyes"></div>
    <div class="cover-art-lower" role="img" aria-label="Palette-knife painting continued, lower part of the face in deep reds and navy"></div>

    <div class="title-band">
      <svg viewBox="0 0 720 170" preserveAspectRatio="none" aria-hidden="true">
        <defs>
          <linearGradient id="band-fill" x1="0" y1="0" x2="0" y2="1">
            <stop offset="0" stop-color="var(--band-shade)"/>
            <stop offset="0.28" stop-color="var(--band-white)"/>
            <stop offset="0.82" stop-color="var(--band-white)"/>
            <stop offset="1" stop-color="#dcdcdc"/>
          </linearGradient>
        </defs>
        <path fill="url(#band-fill)" d="M0 10 L30 6 L52 12 L80 7 L110 11 L140 4 L172 10 L200 6 L236 12 L268 5 L300 10 L330 7 L362 13 L398 6 L430 11 L460 5 L496 12 L530 7 L562 11 L596 4 L628 10 L660 6 L690 12 L720 7 L720 158 L694 163 L662 157 L630 164 L598 158 L566 165 L532 159 L500 164 L468 157 L436 163 L402 158 L370 165 L338 159 L304 164 L270 157 L238 163 L204 158 L172 165 L140 159 L108 164 L76 157 L44 163 L20 158 L0 162 Z"/>
      </svg>
      <div class="title-block">
        <h1 class="book-title">The Open Meadow</h1>
        <p class="book-subtitle">Walking Forward Beyond Every Box</p>
      </div>
    </div>

    <p class="author-name">Name name</p>
  </section>
</main>
</body>
</html>
```